Overview of Elder Abuse Resources Brochure

We need a 2-page brochure that provides a list of resources for elders in tribal communities in the US and those who care for them. We want it to be simple and easy to read, and easy to see the difference between each resource. We would also like eye-catching images or graphics. Please keep the images on the front, and add any photos or graphics that depict Native American elders. We need both of our logos on the first page, in the far-right column. Please refer to the attached image for our brand colors and a font suggestion. Please keep the three columns on each page, but delete the blank pages in the document.

```html
<!DOCTYPE html>
<html lang="en">
<head>
<meta charset="utf-8">
<title>Services for Elders &amp; People Who Care for Them — Brochure</title>
<link rel="stylesheet" href="https://fonts.googleapis.com/css2?family=Barlow:wght@300;400;500;600;700&family=Barlow+Semi+Condensed:wght@500;600;700&display=swap">
<style>
:root{
  --teal:#2a7a85;
  --teal-dark:#236a74;
  --red:#b5544c;
  --maroon:#4a1b1b;
  --beige:#ebe7d9;
  --ink:#1d1d1d;
  --rule:#cfc9b8;
  --page:#ffffff;
  --bg:#d6d6d6;
}
*{margin:0;padding:0;box-sizing:border-box}
html,body{width:1200px;height:2336px;overflow:hidden}
body{background:var(--bg);font-family:"Barlow",sans-serif;color:var(--ink);position:relative}
.spread{position:absolute;left:50px;width:1100px;height:778px;display:flex;background:var(--page);box-shadow:0 6px 18px rgba(0,0,0,.25)}
.spread--outside{top:350px}
.spread--inside{top:1208px}
.panel{width:366.67px;height:100%;position:relative;padding:34px 30px 0 34px;overflow:hidden}
.panel--beige{background:var(--beige)}
.border-band{position:absolute;left:0;right:0;bottom:0;height:16px;background:linear-gradient(90deg,#c98a84,#7fb0b5,#c98a84)}
.heading{font-family:"Barlow Semi Condensed",sans-serif;font-weight:700;font-size:26px;line-height:1.2;text-transform:uppercase;color:var(--red)}
.heading .teal{color:var(--teal)}
.body-copy{font-size:15px;line-height:1.25;margin-top:16px}
.body-copy p+p{margin-top:18px}
.contact-box{margin-top:28px;border:1px solid #aaa}
.contact-box__title{background:var(--red);color:#fff;font-family:"Barlow Semi Condensed",sans-serif;font-weight:700;font-size:21px;text-align:center;padding:2px 0}
.contact-box__sub{background:var(--teal-dark);color:#fff;text-align:center;font-size:15px;font-weight:300;line-height:1.25;padding:6px 20px}
.contact-box__fill{color:#aaa;font-weight:300;text-align:center;font-size:15px;line-height:1.25;padding:16px 40px 18px}
.hotlines{margin-top:14px}
.hotline{text-align:center;font-size:15px;line-height:1.25;padding:9px 0;border-bottom:1px solid var(--rule)}
.hotline:last-child{border-bottom:none}
.hotline .num{font-family:"Barlow Semi Condensed",sans-serif;font-weight:700;font-size:20px;color:var(--teal)}
.hotline .hot{color:var(--red);font-weight:700}
.hotline--big{font-family:"Barlow Semi Condensed",sans-serif;font-weight:700;font-size:20px}
.rot{position:absolute;transform:rotate(-90deg);transform-origin:left top;white-space:nowrap;font-size:15px;line-height:1.2}
.rot .label{color:var(--red);font-weight:700}
.mailer-name{position:absolute;left:292px;top:300px;transform:rotate(-90deg);transform-origin:left top;white-space:nowrap;font-family:"Barlow Semi Condensed",sans-serif;font-weight:700;font-size:20px;color:var(--teal);display:flex;align-items:center;gap:10px}
.dot{display:inline-block;width:14px;height:14px;border-radius:50%;background:var(--teal)}
.cover{padding:0}
.cover__brands{height:158px;display:flex;align-items:center;justify-content:center}
.brand{flex:1;text-align:center;font-family:"Barlow Semi Condensed",sans-serif;font-weight:700;font-size:17px;line-height:1.15;color:var(--teal);padding:0 12px;display:flex;flex-direction:column;align-items:center;gap:8px}
.brand--gold{color:#b89a5a}
.brand--gold .dot{background:#b89a5a}
.brand-divider{width:1px;height:100px;background:#bbb}
.pattern-band{height:18px;background:linear-gradient(90deg,#e0b2ac,#c97a72,#e0b2ac)}
.pattern-band--teal{height:20px;background:linear-gradient(90deg,#a8d0d4,#4f9ba3,#a8d0d4)}
.cover__title{background:var(--maroon);color:#fff;text-align:center;padding:20px 10px 18px;height:148px}
.cover__title h1{font-family:"Barlow Semi Condensed",sans-serif;font-weight:500;font-size:28px;line-height:1.2}
.cover__title .who{font-family:"Barlow Semi Condensed",sans-serif;font-size:13px;margin-top:16px;word-spacing:2px}
.cover__photo{height:294px;background:linear-gradient(160deg,#c46a3a 0%,#b3532c 45%,#7a3a6a 70%,#d98a4a 100%)}
.cover__lines{text-align:center;font-family:"Barlow Semi Condensed",sans-serif;font-size:13px;line-height:1;padding-top:28px}
.cover__lines p{margin-bottom:17px}
.resources{margin-top:10px}
.resource{padding:11px 0;border-bottom:1px solid var(--rule);font-size:14.5px;line-height:1.25;overflow-wrap:anywhere}
.resource:last-child{border-bottom:none}
.resource h3{font-family:"Barlow Semi Condensed",sans-serif;font-weight:700;font-size:15.5px;color:var(--teal);line-height:1.2}
.resource .lite{font-weight:300}
.resource .strong{font-weight:500}
.subhead{font-family:"Barlow Semi Condensed",sans-serif;font-weight:600;font-size:21px;color:var(--teal);line-height:1.15;margin-top:6px}
.stories{list-style:none;margin-top:22px;font-size:15px;line-height:1.25}
.stories li{position:relative;padding-left:18px;margin-bottom:15px}
.stories li::before{content:"•";position:absolute;left:0}
.group-photo{position:absolute;left:0;right:0;bottom:16px;height:250px}
.group-photo__fill{height:232px;background:linear-gradient(180deg,#3f5a2e 0%,#5d6b3a 45%,#b07a68 75%,#c4a58a 100%)}
</style>
</head>
<body>

<section class="spread spread--outside" aria-label="Brochure outside">
  <div class="panel respect">
    <h2 class="heading"><span class="teal">Respect for</span> Elders</h2>
    <div class="body-copy">
      <p>Do you have concerns about an Elder, maybe you see that they are not taking care of themselves, or family only comes once a month when the Elder has money?</p>
      <p>Is an Elder telling you that they are not treated with respect or that someone is bothering them?</p>
      <p>These may be signs of Elder abuse, neglect or exploitation.</p>
    </div>
    <div class="contact-box">
      <div class="contact-box__title">FOR HELP, CONTACT</div>
      <div class="contact-box__sub">Your Tribal Social Services or Elders Department:</div>
      <div class="contact-box__fill">Insert contact information for your tribal services, law enforcement, etc.</div>
    </div>
    <div class="hotlines">
      <div class="hotline">The Elder Help Finder for information<br>on Adult Protective Services<br><span class="num">1-800-555-0142</span></div>
      <div class="hotline hotline--big">If a serious emergency, <span class="hot">call 911.</span></div>
      <div class="hotline">For mental health support for yourself<br>or an Elder, <span class="hot">call or text 555-0199</span></div>
      <div class="hotline">Domestic Violence Hotline<br><span class="num">1.800.555.CARE (2273)</span></div>
    </div>
  </div>

  <div class="panel panel--beige mailer">
    <div class="mailer-name"><span class="dot"></span>Circle of Elders Alliance</div>
    <div class="rot" style="left:158px;top:452px"><span class="label">Recipient</span><br>Street Address<br>City, ST ZIP Code</div>
    <div class="rot" style="left:42px;top:700px"><span class="label">Company Name</span><br>Street Address<br>City, ST ZIP</div>
  </div>

  <div class="panel cover">
    <div class="cover__brands">
      <div class="brand"><span class="dot"></span>Circle of Elders Alliance</div>
      <div class="brand-divider"></div>
      <div class="brand brand--gold"><span class="dot"></span>Tribal Elder Care Network</div>
    </div>
    <div class="pattern-band" role="img" aria-label="Zigzag border pattern"></div>
    <div class="cover__title">
      <h1>Services for Elders &amp;<br>People Who Care for Them</h1>
      <p class="who">My Mother &nbsp;| &nbsp;My Father | &nbsp;My Sister | &nbsp;My Grandchild | &nbsp;Myself</p>
    </div>
    <div class="pattern-band pattern-band--teal" role="img" aria-label="Zigzag border pattern"></div>
    <div class="cover__photo" role="img" aria-label="Photo of two Native American elder women outside a traditional earthen hogan in red desert light"></div>
    <div class="cover__lines">
      <p>Are you caring for an Elder or a Grandchild?</p>
      <p>Are you an Elder who needs help staying at home?</p>
      <p>These programs and information can be a helpful resource.</p>
    </div>
  </div>
  <div class="border-band" role="img" aria-label="Zigzag border pattern"></div>
</section>

<section class="spread spread--inside" aria-label="Brochure inside">
  <div class="panel stories-panel">
    <h2 class="heading">Do these stories sound<br>familiar to you?</h2>
    <ul class="stories">
      <li>My mother gets lost driving home from the store.</li>
      <li>I need help getting groceries and with chores at home.</li>
      <li>My dad wants to sleep all the time; he doesn’t go out with friends anymore. He stopped drumming.</li>
      <li>My sister is raising 3 grandchildren on her own.</li>
      <li>My son is disrespecting me. He only comes to visit when my retirement money arrives. He always asks for money.</li>
    </ul>
    <div class="group-photo">
      <div class="pattern-band" role="img" aria-label="Zigzag border pattern"></div>
      <div class="group-photo__fill" role="img" aria-label="Group photo of Native American elders standing together outdoors in front of greenery"></div>
    </div>
  </div>

  <div class="panel panel--beige">
    <h2 class="heading">Resources for Elders</h2>
    <div class="resources">
      <div class="resource">
        <h3>Elder Help Finder</h3>
        <p class="strong">https://elderhelpfinder.example.org/home<br>Call or Text: 1-800-555-0142<br>Email: help@elderhelpfinder.example.org</p>
        <p class="lite">For help finding support. Ask about services to Tribal Elders.</p>
      </div>
      <div class="resource">
        <h3>Memory Care Help Center</h3>
        <p class="strong">Call 1-800-555-0178. (Available 24/7)</p>
        <p class="lite">Connect with a live person who can provide information, local resources, crisis assistance and emotional support on Alzheimer’s and Dementia.</p>
      </div>
      <div class="resource">
        <h3>Crisis Support Lifeline</h3>
        <p class="lite">For mental health support, <span class="strong">call or text 555-0199.</span></p>
      </div>
      <div class="resource">
        <h3>State &amp; Tribal Hotlines | Tribal Elder Care Network</h3>
        <p class="lite">To find local resources within your tribe or state that specialize in elder abuse, neglect or exploitation, visit:</p>
        <p class="strong">https://tribalcare.example.org/hotlines/state-tribal/</p>
      </div>
      <div class="resource">
        <h3>Heartline Native Helpline</h3>
        <p class="lite">A 24/7 safe, confidential and anonymous domestic and sexual violence helpline for Native Americans and Alaska Natives.</p>
        <p class="strong">Call 1-844-555-0123<br>https://heartline.example.org/</p>
      </div>
    </div>
  </div>

  <div class="panel">
    <h2 class="heading">Resources for<br>Caregivers</h2>
    <p class="subhead">Caring for an Older Adult</p>
    <div class="resources">
      <div class="resource">
        <h3>Elder Help Finder</h3>
        <p class="strong">https://elderhelpfinder.example.org/home<br>Call or Text: 1-800-555-0142<br>Email: help@elderhelpfinder.example.org</p>
        <p class="lite">For help finding support. Ask about services to Tribal Elders.</p>
      </div>
      <div class="resource">
        <h3>Memory Friends | Circle of Elders Alliance</h3>
        <p class="lite">An interactive educational program to better understand what dementia is and how it affects people.</p>
        <p class="strong">https://circleofelders.example.org/memory-friends/</p>
      </div>
    </div>
    <p class="subhead">Grandparents Raising<br>Grandchildren (Kinship Care)</p>
    <div class="resources">
      <div class="resource">
        <h3>KinFamilies.example.org</h3>
        <p class="lite">An interactive website that seeks to share all relevant publicly available information impacting grandfamilies.</p>
      </div>
      <div class="resource">
        <h3>Grandparent Resources | Tribal Elder Care Network</h3>
        <p class="lite">A list of resources for grandparents raising grandchildren.</p>
        <p class="strong">https://tribalcare.example.org/<br>resource/grandparents/</p>
      </div>
    </div>
  </div>
  <div class="border-band" role="img" aria-label="Zigzag border pattern"></div>
</section>

</body>
</html>
```